Business Card design, larkwell shipping

I started a container shipping company which specialized in export of cars, motorcycles, boats and general cargo overseas. I need a business card that stands out of the pack and gives clients an idea of what I do. I have attached a sample that someone designed for me but I don't think its the right fit. However the info on it is accurate so can be used right on new card.
Updates

Reason: I would like my new logo which is being designed on PLANOVISTRA.COM as well to be implemented into my business card.

Industry/Entity Type

Shipping

```html
<!DOCTYPE html>
<html lang="en">
<head>
<meta charset="utf-8">
<title>Larkwell Shipping – Business Card</title>
<link href="https://fonts.googleapis.com/css2?family=Source+Sans+3:wght@400;600;700&display=swap" rel="stylesheet">
<style>
  :root {
    --sand: #e3d7ce;
    --wine: #561c20;
    --wine-text: #5a1a1e;
    --ink: #5b504a;
    --rule: #c4b5a8;
    --ghost-light: #d0c3b9;
    --ghost-dark: #6b2e30;
    --collage: #5f2226;
    --white: #ffffff;
  }
  * { box-sizing: border-box; margin: 0; padding: 0; }
  html, body { width: 1200px; height: 1200px; overflow: hidden; }
  body {
    position: relative;
    background: var(--white);
    font-family: "Source Sans 3", "Myriad Pro", sans-serif;
  }
  .top-band {
    position: absolute; left: 0; top: 0; width: 1200px; height: 100px;
    background: var(--sand);
    display: flex; align-items: center; justify-content: center;
  }
  .brand-name {
    font-weight: 700; color: var(--wine-text); letter-spacing: 0.2px;
    display: flex; align-items: center; gap: 6px; white-space: nowrap;
  }
  .brand-dot { width: 10px; height: 10px; border-radius: 50%; background: currentColor; flex: none; }
  .top-band .brand-name { font-size: 16px; }
  .bottom-band {
    position: absolute; left: 0; top: 1099px; width: 1200px; height: 101px;
    background: var(--sand);
    display: flex; align-items: center; justify-content: center;
    font-size: 17px; color: var(--wine-text);
  }
  .card {
    position: absolute; top: 348px; width: 288px; height: 504px;
    border-radius: 22px; overflow: hidden;
  }
  .card-front { left: 299px; background: var(--sand); }
  .card-back { left: 612px; background: var(--wine); }
  .emblem-area {
    position: absolute; top: 10px; width: 180px; height: 150px; border-radius: 40px;
  }
  .card-front .emblem-area { left: 108px; background: radial-gradient(ellipse at center, var(--ghost-light) 0%, rgba(208,195,185,0) 70%); }
  .card-back .emblem-area { left: 0; background: radial-gradient(ellipse at center, var(--ghost-dark) 0%, rgba(107,46,48,0) 70%); }
  .collage-area {
    position: absolute; left: 0; top: 168px; width: 288px; height: 160px;
    background: linear-gradient(180deg, rgba(95,34,38,0) 0%, var(--collage) 30%, var(--collage) 70%, rgba(95,34,38,0) 100%);
  }
  .card-front .brand-name { position: absolute; left: 21px; top: 226px; font-size: 13px; }
  .person { position: absolute; left: 21px; top: 298px; }
  .person-name { font-size: 23px; font-weight: 700; color: var(--ink); line-height: 1; letter-spacing: -0.3px; }
  .person-role { font-size: 11.5px; color: var(--ink); margin-top: 2px; }
  .rule { position: absolute; left: 21px; width: 256px; border-top: 1px dashed var(--rule); }
  .contacts { position: absolute; left: 21px; top: 348px; list-style: none; }
  .contacts li {
    display: flex; align-items: center; gap: 8px;
    font-size: 11.5px; color: var(--ink); height: 21.5px;
  }
  .contacts svg { width: 9px; height: 9px; fill: var(--ink); flex: none; }
  .address { position: absolute; left: 21px; top: 447px; font-size: 11.5px; color: var(--ink); line-height: 15px; }
  .tab { position: absolute; left: 55px; top: 492px; width: 178px; height: 20px; border-radius: 10px 10px 0 0; }
  .card-front .tab { background: var(--wine); }
  .card-back .tab { background: var(--sand); }
  .card-back .brand-name { position: absolute; left: 0; right: 0; top: 392px; justify-content: center; color: var(--sand); font-size: 13px; }
  .card-back .site { position: absolute; left: 0; right: 0; top: 464px; text-align: center; font-size: 11.5px; color: var(--sand); }
</style>
</head>
<body>
  <header class="top-band">
    <div class="brand-name"><span class="brand-dot"></span>LARKWELL SHIPPING</div>
  </header>

  <section class="card card-front">
    <div class="emblem-area" role="img" aria-label="Faint brand emblem decoration"></div>
    <div class="brand-name"><span class="brand-dot"></span>LARKWELL SHIPPING</div>
    <div class="person">
      <div class="person-name">MAREK SOLLEN</div>
      <div class="person-role">Chief Operating Officer</div>
    </div>
    <div class="rule" style="top:343px"></div>
    <ul class="contacts">
      <li><svg viewBox="0 0 10 10"><path d="M3 0h2l1 3-1.5 1a6 6 0 0 0 1.5 1.5L7 4l3 1v2c0 1-1 3-3 3C3 10 0 7 0 3c0-2 2-3 3-3z"/></svg>1-555-014-2286</li>
      <li><svg viewBox="0 0 10 10"><path d="M2 0h6v10H2zM3 1v6h4V1z"/></svg>1-555-019-7734</li>
      <li><svg viewBox="0 0 10 10"><path d="M0 2h10v7H0zM1 3l4 3 4-3z"/></svg>marek@larkwellgroup.com</li>
      <li><svg viewBox="0 0 10 10"><circle cx="5" cy="5" r="5"/></svg>www.larkwellgroup.com</li>
    </ul>
    <div class="rule" style="top:438px"></div>
    <div class="address">2480 Harbor Lane Unit 4b<br>Bayford, NJ 07990</div>
    <div class="tab"></div>
  </section>

  <section class="card card-back">
    <div class="emblem-area" role="img" aria-label="Faint brand emblem decoration"></div>
    <div class="collage-area" role="img" aria-label="Tone-on-tone typographic collage of port city names"></div>
    <div class="brand-name"><span class="brand-dot"></span>LARKWELL SHIPPING</div>
    <div class="site">www.larkwellgroup.com</div>
    <div class="tab"></div>
  </section>

  <footer class="bottom-band">www.larkwellgroup.com</footer>
</body>
</html>
```